LH Business Card NEEDED

Lumen Harbour is a finance brokering company that provide lending advise to consumer, business, corporate, and property developer for all their financing needs.

We source and match customer needs in Home Loan, Business Loan, Commercial Property Loan, Assets Finance, and other banking related services. It is a market with full of loans! But we specialise in more complex loan structure and our client base are more business and corporate level. Our suppliers are Banks and large Financial Institution where these business card will go to.

We have a great deal of Asian clients, therefore the card need to also include Chinese language together with English.

Refer to attached file for logo and content requirements.

We are looking for designs with the following ingredients:
* Innovative & Creative
* Professional
* Trust & Security

Please pick colours that will compliment the colours of the company logo.

Please provide a unique design, for example the edge of the card is rounded or corner cut off.
Updates

Company logo uploaded.

Please commence submitting your design.

Target Market(s)

Target audiences are businessmen, corporate, and property developer. And also a great deal of Chinese clients.

Industry/Entity Type

Finance

Contact Information for Business Card

Lumen Harbour Pty. Ltd.
Morris Okafor
Director
Suite 42, 7-9 Pellow St. Dunmore NSW 2738

Requirements
Must have
• Double sided design

```html
<!DOCTYPE html>
<html lang="en">
<head>
<meta charset="utf-8">
<title>Lumen Harbour Business Card</title>
<link rel="stylesheet" href="https://fonts.googleapis.com/css2?family=Cinzel:wght@400&family=Noto+Serif:wght@400;700&family=Noto+Serif+SC:wght@400;600&display=swap">
<style>
  :root {
    --stage: #1f1f20;
    --gold-dark: #b98f2a;
    --gold-mid: #d9b551;
    --gold-light: #f3e3a0;
    --silver-dark: #8e9094;
    --silver-light: #e6e7e9;
    --paper: #ffffff;
    --ink: #1b1710;
    --rule: #9a9a9a;
  }
  * { box-sizing: border-box; margin: 0; padding: 0; }
  html, body { width: 1200px; height: 900px; overflow: hidden; }
  body {
    background: var(--stage);
    font-family: "Noto Serif", "Noto Serif SC", serif;
    color: var(--ink);
    position: relative;
  }
  .card {
    position: absolute;
    top: 300px;
    width: 500px;
    height: 300px;
    border-radius: 30px;
    overflow: hidden;
    box-shadow: 0 18px 40px rgba(0,0,0,0.55);
  }
  .card-front { left: 60px; }
  .card-back { left: 640px; background: var(--paper); }
  .gold-surface {
    background: linear-gradient(90deg, var(--gold-dark) 0%, var(--gold-light) 22%, var(--gold-mid) 45%, var(--gold-light) 70%, var(--gold-dark) 100%);
  }
  .card-front { }
  .brand-mark {
    position: absolute;
    left: 50%;
    transform: translateX(-50%);
    border-radius: 50%;
    background: var(--silver-dark);
  }
  .card-front .brand-mark { top: 44px; width: 110px; height: 110px; }
  .brand-name {
    position: absolute;
    left: 0; right: 0;
    text-align: center;
    font-family: "Cinzel", serif;
    font-weight: 400;
    color: var(--ink);
    text-transform: uppercase;
    white-space: nowrap;
  }
  .card-front .brand-name { top: 176px; font-size: 24px; letter-spacing: 11px; }
  .brand-rule {
    position: absolute;
    left: 50%;
    transform: translateX(-50%);
    height: 1px;
    background: linear-gradient(90deg, transparent, var(--rule), transparent);
  }
  .card-front .brand-rule { top: 212px; width: 360px; }
  .brand-name-cn {
    position: absolute;
    left: 0; right: 0;
    text-align: center;
    font-family: "Noto Serif SC", serif;
    font-weight: 400;
    color: var(--ink);
  }
  .card-front .brand-name-cn { top: 214px; font-size: 30px; letter-spacing: 4px; }

  .card-back .brand-mark { top: 24px; width: 64px; height: 64px; }
  .card-back .brand-name { top: 100px; font-size: 15px; letter-spacing: 8px; }
  .card-back .brand-rule { top: 122px; width: 230px; }
  .card-back .brand-name-cn { top: 122px; font-size: 18px; letter-spacing: 3px; }
  .silver-band {
    position: absolute;
    left: 0; right: 0;
    top: 160px;
    height: 7px;
    background: linear-gradient(90deg, var(--silver-dark), var(--silver-light) 50%, var(--silver-dark));
  }
  .contact-panel {
    position: absolute;
    left: 0; right: 0; top: 167px; bottom: 0;
    text-align: center;
    padding-top: 10px;
    line-height: 1.25;
  }
  .person-name { font-size: 22px; font-weight: 700; }
  .person-name .cn, .cn { font-family: "Noto Serif SC", serif; font-size: 11px; font-weight: 400; }
  .person-title { font-size: 12px; }
  .company-line { font-size: 12px; margin-top: 6px; }
  .address-line { font-size: 12px; font-weight: 700; }
  .address-cn { font-family: "Noto Serif SC", serif; font-size: 11px; }
</style>
</head>
<body>
  <section class="card card-front gold-surface" aria-label="Business card front">
    <div class="brand-mark"></div>
    <div class="brand-name">Lumen Harbour</div>
    <div class="brand-rule"></div>
    <div class="brand-name-cn">明港通</div>
  </section>

  <section class="card card-back" aria-label="Business card back">
    <div class="brand-mark"></div>
    <div class="brand-name">Lumen Harbour</div>
    <div class="brand-rule"></div>
    <div class="brand-name-cn">明港通</div>
    <div class="silver-band"></div>
    <div class="contact-panel gold-surface">
      <p class="person-name">Morris Okafor <span class="cn">(莫里斯·奥卡福)</span></p>
      <p class="person-title">Director <span class="cn">(董事)</span></p>
      <p class="company-line">Lumen Harbour Pty. Ltd. <span class="cn">(明港金融有限公司 贷款顾问)</span></p>
      <p class="address-line">Suite 42, 7-9 Pellow St. Dunmore NSW 2738</p>
      <p class="address-cn">(邓莫尔 佩洛街 7-9 号 42 室 NSW 2738)</p>
    </div>
  </section>
</body>
</html>
```